Nimbus Crest Plan- Brindlow Insurance providing specialist Cyber and Liability Insurance

for Managed Technology Service Providers and their customer, we will use a letterhead that white labels insurer documents, which can be used in our physical letters as well as to be used within Email signatures.

Target Market(s)

Managed Technology Services Providers

Industry/Entity Type

Cyber Insurance

Requirements
Must have
• website, email address, contact phone numbers

```html
<!DOCTYPE html>
<html lang="en">
<head>
<meta charset="utf-8">
<title>Nimbus Crest Plan – Letterhead</title>
<link href="https://fonts.googleapis.com/css2?family=Arimo:wght@400;700&family=Mulish:wght@700;800&display=swap" rel="stylesheet">
<style>
  :root {
    --backdrop: #dedede;
    --paper: #ffffff;
    --ink: #4a4a4a;
    --ink-dark: #3f3f3f;
    --brand-green: #39b54a;
    --brand-grey: #474747;
  }
  * { box-sizing: border-box; margin: 0; padding: 0; }
  html, body {
    width: 1200px; height: 1200px; overflow: hidden;
    background: var(--backdrop);
  }
  .letterhead {
    position: absolute; left: 223px; top: 67px;
    width: 754px; height: 1065px;
    background: var(--paper);
    font-family: "Arimo", Arial, sans-serif;
    color: var(--ink);
  }
  .header { position: absolute; left: 59px; top: 58px; width: 636px; height: 52px; }
  .brand-name {
    position: absolute; left: 0; top: 12px;
    font-family: "Arimo", Arial, sans-serif; font-weight: 700;
    font-size: 26px; letter-spacing: 0.5px; color: var(--ink-dark);
    white-space: nowrap;
  }
  .divider { position: absolute; top: 2px; width: 1px; height: 41px; background: var(--ink); }
  .divider--contact { left: 320px; }
  .divider--address { left: 520px; }
  .contact-list { position: absolute; left: 348px; top: 0; list-style: none; font-size: 12.5px; line-height: 15px; }
  .contact-list li { display: flex; align-items: center; gap: 8px; white-space: nowrap; }
  .contact-list svg { width: 10px; height: 10px; flex: none; }
  .address { position: absolute; left: 552px; top: 0; font-size: 12.5px; line-height: 15px; font-style: normal; white-space: nowrap; }
  .header-rule { position: absolute; left: 59px; top: 109px; width: 637px; height: 1px; background: var(--ink-dark); }

  .salutation {
    position: absolute; left: 69px; top: 327px;
    font-family: "Mulish", "Century Gothic", sans-serif; font-weight: 800;
    font-size: 17px; color: var(--ink);
  }
  .body-copy { position: absolute; left: 67px; top: 376px; width: 624px; font-size: 12.8px; line-height: 15.5px; }
  .body-copy p { margin-bottom: 13.5px; }
  .closing {
    position: absolute; left: 69px; top: 697px;
    font-family: "Mulish", "Century Gothic", sans-serif; font-weight: 800; font-size: 10px;
  }
  .signature { position: absolute; left: 65px; top: 738px; width: 116px; height: 34px; background: linear-gradient(90deg, #f1f1f1, #e6e6e6); }
  .footer-band { position: absolute; left: 0; bottom: 0; width: 754px; height: 14px; }
</style>
</head>
<body>
  <main class="letterhead">
    <header class="header">
      <div class="brand-name">Nimbus Crest Plan</div>
      <span class="divider divider--contact"></span>
      <ul class="contact-list">
        <li>
          <svg viewBox="0 0 10 10" aria-hidden="true"><path d="M2 1 L4 3 L3 4 Q4 6 6 7 L7 6 L9 8 L8 9 Q3 9 1 2 Z" fill="var(--brand-green)"/></svg>
          123-456-2100
        </li>
        <li>
          <svg viewBox="0 0 10 10" aria-hidden="true"><rect x="0.5" y="2" width="9" height="6.5" fill="var(--brand-green)"/><path d="M0.5 2 L5 5.8 L9.5 2" stroke="#fff" stroke-width="0.9" fill="none"/></svg>
          youremail@mailbox.com
        </li>
        <li>
          <svg viewBox="0 0 10 10" aria-hidden="true"><circle cx="5" cy="5" r="4.5" fill="var(--brand-green)"/><path d="M0.5 5 H9.5 M5 0.5 V9.5" stroke="#fff" stroke-width="0.8"/></svg>
          www.yourwebsite.com
        </li>
      </ul>
      <span class="divider divider--address"></span>
      <address class="address">Your address<br>city<br>state, ZIP 0000</address>
    </header>
    <div class="header-rule"></div>

    <h1 class="salutation">Dear Mr. Smith,</h1>

    <section class="body-copy">
      <p>Lorem ipsum dolor sit amet, consectetuer adipiscing elit, sed diam nonmmy nibh euismod tincidunt ut laor eet dolore magna aliquam erat volutpat. Ut wisi enim ad minim veniam, quis nostrud exerci tationmcorper suscipit lobortis nisl ut aliquip ex ea commodo consequat. Duis autem vel eum iriure dolor in hendrerit in vulputate velit esse molestie consequat, vel illum dolore eu feugiat</p>
      <p>Rorem ipsum dolor sit amet, consectetuer adipiscing elit, sed diam nonmmy nibh euismod tincidunt ut laor eet dolore magna aliquam erat volutpat. Ut wisi enim ad minim veniam, quis nostrud exerci tationmcorper suscipit lobortis nisl ut aliquip ex ea commodo consequat. Duis autem vel eum iriure dolor in hendrerit in vulputate velit esse molest</p>
      <p>Dorem ipsum dolor sit amet, consectetuer adipiscing elit, sed diam nonmmy nibh euismod tincidunt ut laor eet dolore magna aliquam erat volutpat. Ut wisi enim ad minim veniam, quis nostrud exerci tationmcorper suscipit lobortis nisl ut aliquip ex ea commodo consequat. Duis autem vel eum iriure dolor in hendrerit in suscipit lobortis nisl ut aliquip ex ea commodo consequat. Duis autem vel eum iriure dolor in hendrerit in vulputate velit esse molestie consequat, vel illum</p>
      <p>Sorem ipsum dolor sit amet, consectetuer adipiscing elit, sed diam nonmmy nibh euismod tincidunt ut laor eet dolore magna aliquam erat volutpat. Ut wisi enim ad minim veniam, quis nostrud exerci tationmcorper suscipit lobortis nisl ut aliquip ex ea commodo consequat. Duis autem vel eum iriure dolor in</p>
    </section>

    <p class="closing">Sincerely,</p>
    <div class="signature" role="img" aria-label="Handwritten signature of the sender"></div>

    <svg class="footer-band" viewBox="0 0 754 14" preserveAspectRatio="none" aria-hidden="true">
      <polygon points="0,0 557,0 545,14 0,14" fill="var(--brand-green)"/>
      <polygon points="568,0 754,0 754,14 556,14" fill="var(--brand-grey)"/>
    </svg>
  </main>
</body>
</html>
```